"Grandpa's Old Mule" Bookcover 170501

We need a book cover for print edition of the title, "Grandpa's Old Mule". The book is about the life of a man and that of his last dog, told from the perspective of his son. The book is a mix of highly improbable situations and a son's remembrance of his father. We've attached pictures of both the man and the dog, however, they do not have to be used, if it doesn't add to the design. It does provide an idea of what the subjects looked like. The author's name is Rob T. Venster. The publisher will be Quiet Heron Publishers. One book size template uploaded. NOTE: Designer credit will be included in the published work.

Target Market(s)

People who like non-fiction strange family and dog stories

Font styles to use
Serif
Sans Serif

Colors

Designer to choose colors to be used in the design.

Requirements
Must have
• A means of communicating a story about two lifetimes, the man and the dog. Full cover, front, spine and back.
Nice to have
• Man and Dog get equal billing, something that indicates a lifetime of events
Should not have
• A mere collage of the uploaded pics. Those can be used, but don't make it as simple as a photo album.

```html
<!DOCTYPE html>
<html lang="en">
<head>
<meta charset="utf-8">
<title>Grandpa's Old Mule – Full Cover</title>
<link rel="stylesheet" href="https://fonts.googleapis.com/css2?family=Cinzel:wght@400;500&family=Cardo:wght@700&family=Lato:wght@400&display=swap">
<style>
  :root {
    --sky-top: #5a2d1d;
    --sky-mid: #b8461a;
    --sky-glow: #f28a1c;
    --sun: #ffe45a;
    --ground: #000000;
    --ink-light: #ffffff;
    --ink-soft: #fbf4ec;
  }
  html, body {
    margin: 0;
    padding: 0;
    width: 1200px;
    height: 877px;
    overflow: hidden;
    background: var(--ground);
  }
  .cover {
    position: relative;
    width: 1200px;
    height: 877px;
    overflow: hidden;
  }
  .cover-photo {
    position: absolute;
    inset: 0;
    background:
      radial-gradient(ellipse 260px 160px at 760px 740px, var(--sun) 0%, rgba(255,200,60,0.7) 35%, rgba(242,138,28,0) 100%),
      radial-gradient(ellipse 900px 520px at 720px 720px, var(--sky-glow) 0%, var(--sky-mid) 55%, rgba(184,70,26,0) 100%),
      linear-gradient(180deg, var(--sky-top) 0%, #8a3a1b 35%, var(--sky-mid) 65%, #c8561c 100%);
  }
  .cover-photo::after {
    content: "";
    position: absolute;
    left: 0; right: 0; bottom: 0;
    height: 122px;
    background: var(--ground);
  }
  .back-title {
    position: absolute;
    left: 64px;
    width: 440px;
    top: 100px;
    margin: 0;
    text-align: center;
    font-family: "Cinzel", serif;
    font-weight: 400;
    font-size: 36px;
    color: var(--ink-light);
    text-shadow: 0 1px 3px rgba(0,0,0,0.35);
  }
  .blurb {
    position: absolute;
    left: 62px;
    width: 442px;
    top: 245px;
    margin: 0;
    text-align: center;
    font-family: "Lato", sans-serif;
    font-size: 17px;
    line-height: 22.4px;
    color: var(--ink-soft);
    text-shadow: 0 1px 2px rgba(0,0,0,0.3);
  }
  .barcode-area {
    position: absolute;
    left: 315px;
    top: 714px;
    width: 225px;
    height: 134px;
    background: var(--ink-light);
  }
  .spine-title, .spine-author {
    position: absolute;
    left: 584px;
    width: 32px;
    margin: 0;
    writing-mode: vertical-rl;
    color: var(--ink-light);
    white-space: nowrap;
    line-height: 32px;
  }
  .spine-title {
    top: 52px;
    font-family: "Cinzel", serif;
    font-size: 31px;
  }
  .spine-author {
    top: 628px;
    font-family: "Cardo", serif;
    font-size: 29px;
    font-weight: 400;
  }
  .front-title {
    position: absolute;
    left: 640px;
    width: 540px;
    top: 30px;
    margin: 0;
    text-align: center;
    font-family: "Cinzel", serif;
    font-weight: 400;
    color: var(--ink-light);
    text-shadow: 0 3px 6px rgba(0,0,0,0.45);
  }
  .front-title span { display: block; }
  .front-title .line-long { font-size: 72px; line-height: 104px; }
  .front-title .line-short { font-size: 112px; line-height: 114px; }
  .front-author {
    position: absolute;
    left: 660px;
    width: 514px;
    top: 780px;
    margin: 0;
    text-align: center;
    font-family: "Cardo", serif;
    font-weight: 700;
    font-size: 43px;
    color: var(--ink-light);
  }
</style>
</head>
<body>
  <main class="cover">
    <div class="cover-photo" role="img" aria-label="Wraparound sunset photograph: orange sky over a dark grassy horizon with silhouettes of a seated dog and a man on the front panel"></div>

    <section class="back-cover">
      <h2 class="back-title">Grandpa's Old Mule</h2>
      <p class="blurb">Lorem ipsum dolor sit amet, consectetuer adipiscing elit. Aenean commodo ligula eget dolor. Aenean massa. Cum sociis natoque penatibus et magnis dis parturient montes, nascetur ridiculus mus. Donec quam felis, ultricies nec, pellentesque eu, pretium quis, sem. Nulla consequat massa quis enim. Donec pede justo, fringilla vel, aliquet nec, vulputate eget, arcu. In enim justo, rhoncus ut, imperdiet a, venenatis vitae, justo. Nullam dictum felis eu pede mollis pretium. Integer tincidunt. Cras dapibus. Vivamus elementum semper nisi. Aenean vulputate eleifend tellus. Aenean leo ligula, porttitor eu, consequat vitae, eleifend ac, enim</p>
      <div class="barcode-area" aria-hidden="true"></div>
    </section>

    <section class="spine">
      <p class="spine-title">GRANDPA'S OLD MULE</p>
      <p class="spine-author">Rob T. Venster</p>
    </section>

    <section class="front-cover">
      <h1 class="front-title">
        <span class="line-long">GRANDPA'S</span>
        <span class="line-short">OLD</span>
        <span class="line-short">MULE</span>
      </h1>
      <p class="front-author">Rob T. Venster</p>
    </section>
  </main>
</body>
</html>
```